HVAC Contractor Website Design

We are working with an HVAC contractor in Idaho called KR HVAC.
Some sites to use for content/competitors and inspiration:
https://www.brelvoclimate.com
https://pinemarsh.site/web/contractor/ (lots of contractor website designs we've approved and continue to show clients)
Thank you for taking the time to consider designing a website for us. We are web developers based in Stockton, CA, USA. Most of our projects go through the same process. Understanding this process may help you win a project with us. We custom-code all of our websites in-house. We don’t have any requirements as to what tools you use for your design, but we prefer Figma files. For any design that we label as four-stars, we send it to the client for review. The client picks the final design they want us to use. Once we complete this process, we will continue to show additional clients all the four-star sites and purchase them later. Your designs will have multiple chances to sell. For better chances of success, we ask that you follow these guidelines.
IMAGES:
If you use any images or icons in the design, we ask that you have a link to the asset so we can purchase the image/icon. Most of the designs we submit do not have the customer’s images on them unless they have some great images. Be creative; show us the feeling you are trying to portray with your image choices. Use any royalty-free site you choose. We subscribe to Adobe and mainly use their images, but we can purchase images outside of Adobe.
PLEASE NOTE: we will not submit designs to clients with watermarks on the images.
FONTS:
We ask that you identify the fonts used in the design. This can be done in a message if you want. We typically use Google Fonts and Adobe Fonts.
CONTENT:
We're always open to different content and ideas. We often submit designs with stock images so the client can see our vision. We typically take pictures after the website launch to use their images with our vision. Lorem Ipsum is fine for paragraphs, but we ask that you write the headers in correct English. We want to be able to show the vision and identify the sections of the website.
INSPIRATION:
We typically add a couple of links in the brief of websites we like to help you get started in your design.
REVISIONS:
We do not often ask for revisions of the designs unless we see something in the design that may not appeal to the client. If there are slight changes that we want to make, we do that in the development process.
FEEDBACK:
We rarely give feedback on designs during the design process. We are working on many website projects and do not have the time to provide feedback. We usually respond if your request is well thought out and asks specific questions, but a note asking “feedback, please” usually goes unanswered

```html
<!DOCTYPE html>
<html lang="en">
<head>
<meta charset="utf-8">
<title>KR HVAC — Heating &amp; Cooling</title>
<link href="https://fonts.googleapis.com/css2?family=Lato:wght@400;700&family=Montserrat:wght@600;700;800&display=swap" rel="stylesheet">
<style>
:root{
  --navy:#1d2b4f;
  --blue:#0b6fd4;
  --blue-deep:#0a4fb0;
  --sky:#2bb8f5;
  --orange:#ff6a00;
  --orange-light:#ffa21a;
  --ink:#222;
  --muted:#444;
  --pale:#eaf2fd;
  --black:#0f0f0f;
  --footer:#1b1b1b;
}
*{box-sizing:border-box;margin:0;padding:0}
html,body{width:1200px;height:3224px;overflow:hidden}
body{font-family:'Lato',sans-serif;color:var(--ink);background:#fff;position:relative}
.abs{position:absolute}
h1,h2,h3{font-family:'Montserrat',sans-serif}
.btn{display:inline-block;background:linear-gradient(180deg,var(--orange-light),var(--orange));color:#fff;font:700 15px 'Lato',sans-serif;text-transform:uppercase;padding:0 22px;height:44px;line-height:44px}
.brand{font:800 34px 'Montserrat',sans-serif;color:var(--navy);display:flex;align-items:center;gap:10px;letter-spacing:1px}
.brand .mark{width:14px;height:14px;background:var(--sky)}

/* header */
.topbar{top:0;left:0;width:1200px;height:85px}
.topbar .brand{position:absolute;left:110px;top:22px}
.contact-chip{position:absolute;top:18px;display:flex;align-items:center;gap:12px}
.contact-chip .ico{width:42px;height:42px;border-radius:50%;display:flex;align-items:center;justify-content:center}
.contact-chip small{display:block;font-size:14px;color:#444}
.contact-chip b{font-size:15px;color:var(--navy)}
.nav{top:85px;left:0;width:1200px;height:43px;background:var(--black)}
.nav ul{list-style:none;display:flex;gap:25px;position:absolute;left:111px;top:14px}
.nav li{color:#fff;font-size:13px;text-transform:uppercase}
.nav li.on{color:var(--sky);font-weight:700}
.request{position:absolute;right:0;top:0;width:290px;height:43px;background:linear-gradient(90deg,var(--blue-deep),var(--sky));clip-path:polygon(12px 0,100% 0,100% 100%,0 100%);color:#fff;font:700 13px 'Lato',sans-serif;display:flex;align-items:center;gap:10px;padding-left:40px}

/* hero */
.hero{top:128px;left:0;width:1200px;height:425px;background:linear-gradient(100deg,#a9b6b1 0%,#6d8a86 30%,#2e6fb6 55%,#0b6fd4 75%,#1b8ef0 100%)}
.hero-text{position:absolute;left:640px;width:460px;top:90px;text-align:center;color:#fff}
.hero-text .pre{font:700 29px 'Montserrat',sans-serif}
.hero-text h1{font-size:70px;font-weight:800;line-height:1;margin:4px 0 18px}
.hero-text p{font-size:15px;line-height:28px;margin-bottom:30px}

/* services */
.sec-title{width:1200px;left:0;text-align:center;font-size:36px;font-weight:800;color:var(--navy)}
.services-sub{top:700px;width:1200px;left:0;text-align:center;font-size:15px;color:#333}
.svc{position:absolute;top:764px;width:235px;height:248px;clip-path:polygon(12px 0,100% 0,calc(100% - 12px) 100%,0 100%)}
.svc span{position:absolute;bottom:38px;width:100%;text-align:center;color:#fff;font-size:19px}
.arrow{position:absolute;top:875px}

/* about */
.about{top:1100px;left:0;width:1200px;height:567px;background:var(--pale)}
.about-frame{position:absolute;left:152px;top:78px;width:383px;height:352px;background:#bcc6d1;clip-path:polygon(0 0,100% 0,96% 100%,4% 100%)}
.about-photo{position:absolute;left:112px;top:93px;width:407px;height:395px;background:linear-gradient(135deg,#7f8f95,#3d4b52 55%,#202a33);clip-path:polygon(4% 0,100% 0,96% 100%,0 100%)}
.about-text{position:absolute;left:587px;top:102px;width:498px}
.about-text h2{font-size:36px;font-weight:800;color:var(--navy);margin-bottom:40px}
.about-text .lead{font-weight:700;font-size:15px;line-height:28px;margin-bottom:6px}
.about-text p{font-size:15px;line-height:28px;color:var(--muted);text-align:justify;margin-bottom:36px}

/* blogs */
.blog{position:absolute;top:1829px;width:317px}
.blog .pic{height:250px}
.blog .card{position:relative;margin:-22px 8px 0;background:#fff;box-shadow:0 4px 12px rgba(0,0,0,.15);padding:30px 20px 32px;height:222px}
.blog .meta{font-size:14px;color:#222;margin-bottom:18px}
.blog h3{font:700 16px 'Lato',sans-serif;margin-bottom:16px}
.blog p{font-size:17px;line-height:28px;color:#333}

/* quote */
.quote{top:2375px;left:0;width:1200px;height:503px;background:linear-gradient(110deg,#2aa6ea 0%,#1f7fd6 40%,#0d58c2 70%,#0b3e9a 100%)}
.quote-card{position:absolute;left:113px;top:33px;width:395px;height:435px;background:#fff;padding:38px 33px}
.quote-card h2{font-size:27px;font-weight:800;color:var(--navy);margin-bottom:22px}
.field{height:38px;border:1px solid #ddd;margin-bottom:13px;display:flex;align-items:center;justify-content:space-between;font-size:13px;color:#555;padding-left:16px}
.field .fi{width:30px;height:100%;border-left:1px solid #ddd;display:flex;align-items:center;justify-content:center}
.field.msg{height:90px;align-items:flex-start;padding-top:12px;margin-bottom:22px}
.finance{position:absolute;left:570px;width:550px;top:160px;text-align:center;color:#fff}
.finance h2{font-size:29px;font-weight:800;line-height:40px;margin-bottom:22px;white-space:nowrap;letter-spacing:-0.2px}
.finance p{font-size:15px;line-height:28px;margin:0 auto 18px;width:480px}

/* footer */
.footer{top:2878px;left:0;width:1200px;height:346px;background:var(--footer);color:#fff}
.footer .brand{position:absolute;left:110px;top:52px;color:#fff}
.foot-nav{position:absolute;right:112px;top:70px;display:flex;gap:25px;list-style:none;font-size:13px;text-transform:uppercase}
.rule{position:absolute;left:111px;width:977px;height:1px;background:#444}
.info{position:absolute;top:170px;display:flex;gap:14px}
.info h4{font:700 17px 'Lato',sans-serif;margin-bottom:6px}
.info div{font-size:15px;line-height:26px}
.info a{color:#fff}
.social{position:absolute;right:110px;top:172px;display:flex;gap:8px}
.social span{width:36px;height:36px;border:1.5px solid #fff;border-radius:50%}
.copy{position:absolute;top:300px;width:1200px;text-align:center;font-size:15px}
</style>
</head>
<body>

<header class="abs topbar">
  <div class="brand"><span class="mark"></span>KR HVAC</div>
  <div class="contact-chip" style="left:700px">
    <div class="ico" style="background:var(--blue)">
      <svg width="22" height="22" viewBox="0 0 24 24" fill="none" stroke="#fff" stroke-width="2"><path d="M4 14v-2a8 8 0 0 1 16 0v2"/><rect x="3" y="13" width="4" height="6" rx="1"/><rect x="17" y="13" width="4" height="6" rx="1"/></svg>
    </div>
    <div><small>Sales &amp; Service:</small><b>+1 (208) 555-0147</b></div>
  </div>
  <div class="contact-chip" style="left:915px">
    <div class="ico" style="background:var(--orange)">
      <svg width="22" height="22" viewBox="0 0 24 24" fill="none" stroke="#fff" stroke-width="2"><circle cx="12" cy="12" r="4"/><path d="M16 12v1.5a2.5 2.5 0 0 0 5 0V12a9 9 0 1 0-3.5 7.1"/></svg>
    </div>
    <div><small>Connect with us:</small><b>info@krhvac.com</b></div>
  </div>
</header>

<nav class="abs nav">
  <ul>
    <li class="on">Home</li><li>About</li><li>Residential</li><li>Commercial</li><li>Service &amp; Repair</li><li>Gallery</li><li>Our Blog</li><li>Contact</li>
  </ul>
  <div class="request">
    <svg width="20" height="20" viewBox="0 0 24 24" fill="none" stroke="#fff" stroke-width="1.8"><path d="M14 3H5v18h14V8z"/><path d="M8 10h7M8 14h5"/><path d="M20 12l-6 6-2 .5.5-2 6-6z"/></svg>
    REQUEST SERVICE
  </div>
</nav>

<section class="abs hero" role="img" aria-label="Two HVAC technicians checking an outdoor air conditioning unit with gauges">
  <div class="hero-text">
    <div class="pre">WELCOME TO</div>
    <h1>KR HVAC</h1>
    <p>Lorem ipsum dolor sit amet, consectetur adipiscing elito eiusmod tempor incididunt ut labore et dolore magna aliqua.</p>
    <span class="btn">Read More</span>
  </div>
</section>

<h2 class="abs sec-title" style="top:638px">WHAT WE DO</h2>
<div class="abs services-sub">Our many services include:</div>
<svg class="arrow" style="left:44px" width="24" height="24" viewBox="0 0 24 24" fill="none" stroke="#999" stroke-width="2"><path d="M20 12H4M10 6l-6 6 6 6"/></svg>
<svg class="arrow" style="left:1131px" width="24" height="24" viewBox="0 0 24 24" fill="none" stroke="#222" stroke-width="2"><path d="M4 12h16M14 6l6 6-6 6"/></svg>
<div class="svc" style="left:112px;background:linear-gradient(160deg,#9a8b6a,#3f3c38)" role="img" aria-label="Technician wiring an HVAC unit"><span>HVAC Installation</span></div>
<div class="svc" style="left:357px;background:linear-gradient(160deg,#6b5a44,#5d6166 60%,#3a3d40)" role="img" aria-label="Outdoor heating units"><span>Heating</span></div>
<div class="svc" style="left:601px;background:linear-gradient(160deg,#b9b2a8,#7b7670 60%,#4a4644)" role="img" aria-label="Hands adjusting plumbing pipes"><span>Plumbing</span></div>
<div class="svc" style="left:845px;background:linear-gradient(160deg,#a66c4f,#5b6f86 55%,#3a4352)" role="img" aria-label="Technician repairing an outdoor HVAC unit"><span>HVAC Repair</span></div>

<section class="abs about">
  <div class="about-frame"></div>
  <div class="about-photo" role="img" aria-label="Technician in a cap servicing an air conditioner coil"></div>
  <div class="about-text">
    <h2>ABOUT US</h2>
    <div class="lead">Lorem ipsum dolor sit amet, consectetur adipiscing elit, sed do eiusmod tempor incididunt ut labore et dolore magna aliqua.</div>
    <p>Lorem ipsum dolor sit amet, consectetur adipiscing elit, sed do eiusmod tempor incididunt ut labore et dolore magna aliqua. Ut enim ad minim veniam, quis nostrud exercitation ullamco laboris nisi ut aliquip ex ea commodo consequat. Duis aute irure dolor in reprehenderit in voluptate velit esse cillum dolore eu fugiat nulla pariatur.</p>
    <span class="btn">Read More</span>
  </div>
</section>

<h2 class="abs sec-title" style="top:1737px;left:-35px">OUR BLOGS</h2>
<article class="blog" style="left:111px">
  <div class="pic" style="background:linear-gradient(135deg,#c9cfd4,#7c8790 50%,#4b5560)" role="img" aria-label="Technician checking refrigerant gauges on rooftop units"></div>
  <div class="card"><div class="meta">10-09-2024 | By Mara Ellison</div><h3>Lorem ipsum dolor sit amet</h3><p>Sed ut perspiciatis unde omnis iste natus error sit voluptatem accusa ntium doloremque</p></div>
</article>
<article class="blog" style="left:442px">
  <div class="pic" style="background:linear-gradient(135deg,#f1ebe2,#d9cdbd 50%,#b8aa97)" role="img" aria-label="Family reading together in a comfortable living room"></div>
  <div class="card"><div class="meta">10-09-2024 | By Mara Ellison</div><h3>Lorem ipsum dolor sit amet</h3><p>Sed ut perspiciatis unde omnis iste natus error sit voluptatem accusan tium doloremque</p></div>
</article>
<article class="blog" style="left:771px">
  <div class="pic" style="background:linear-gradient(135deg,#e9ecef,#b9c0c7 50%,#8a3a32)" role="img" aria-label="Technician adjusting a wall-mounted boiler"></div>
  <div class="card"><div class="meta">10-09-2024 | By Mara Ellison</div><h3>Lorem ipsum dolor sit amet</h3><p>Sed ut perspiciatis unde omnis iste natus error sit voluptatem accusan tium doloremque</p></div>
</article>

<section class="abs quote" role="img" aria-label="Blue-tinted row of outdoor condenser units">
  <form class="quote-card">
    <h2>GET A QUOTE</h2>
    <div class="field">Name<span class="fi"><svg width="14" height="14" viewBox="0 0 24 24" fill="none" stroke="#999" stroke-width="2"><circle cx="12" cy="8" r="4"/><path d="M4 21c1-5 15-5 16 0"/></svg></span></div>
    <div class="field">Service<span class="fi"><svg width="14" height="14" viewBox="0 0 24 24" fill="none" stroke="#999" stroke-width="2"><circle cx="12" cy="12" r="3"/><circle cx="12" cy="12" r="8"/></svg></span></div>
    <div class="field">Email Address<span class="fi"><svg width="14" height="14" viewBox="0 0 24 24" fill="none" stroke="#999" stroke-width="2"><rect x="3" y="6" width="18" height="12"/><path d="M3 6l9 7 9-7"/></svg></span></div>
    <div class="field msg">Message</div>
    <span class="btn">Read More</span>
  </form>
  <div class="finance">
    <h2>FLEXIBLE FINANCING OPTIONS<br>FOR YOUR HVAC NEEDS</h2>
    <p>Lorem ipsum dolor sit amet, consectetur adipiscing elito eiusmod lorem tempor incididunt ut labore et dolore magna aliqua.</p>
    <span class="btn">Read More</span>
  </div>
</section>

<footer class="abs footer">
  <div class="brand"><span class="mark"></span>KR HVAC</div>
  <ul class="foot-nav"><li>Home</li><li>About</li><li>Residential</li><li>Commercial</li><li>Service &amp; Repair</li><li>Our Blog</li><li>Contact</li></ul>
  <div class="rule" style="top:140px"></div>
  <div class="info" style="left:111px">
    <svg width="20" height="22" viewBox="0 0 24 24" fill="none" stroke="#fff" stroke-width="1.8"><path d="M12 22s7-7 7-12a7 7 0 0 0-14 0c0 5 7 12 7 12z"/><circle cx="12" cy="10" r="2.5"/></svg>
    <div><h4>ADDRESS</h4>KR HVAC, address comes here<br><a href="#">View Map</a></div>
  </div>
  <div class="info" style="left:428px">
    <svg width="24" height="22" viewBox="0 0 24 24" fill="none" stroke="#fff" stroke-width="1.8"><rect x="2" y="5" width="20" height="14"/><path d="M2 5l10 8 10-8"/></svg>
    <div><h4>EMAIL</h4>info@krhvac.com</div>
  </div>
  <div class="info" style="left:674px">
    <svg width="22" height="22" viewBox="0 0 24 24" fill="none" stroke="#fff" stroke-width="1.8"><path d="M5 3h4l2 5-2.5 1.5a11 11 0 0 0 6 6L16 13l5 2v4a2 2 0 0 1-2 2A17 17 0 0 1 3 5a2 2 0 0 1 2-2z"/></svg>
    <div><h4>PHONE</h4>+1 (208) 555-0147</div>
  </div>
  <div class="social"><span></span><span></span><span></span><span></span></div>
  <div class="rule" style="top:268px"></div>
  <div class="copy">2024 KR HVAC. All Rights Reserved.</div>
</footer>

</body>
</html>
```